Unique business card design

We are looking for a design that reflects our unique social media and online marketing agency "Kestrel Media". We are a young agency with a focus on speakers, coaches and trainers. In other words, we support people who want to do good with their work and help other people live a happier, more successful and fulfilling life, reach as many people as possible with their work and thus have an influence. Our values are: sustainability, creating added value, individuality, proactivity. We want our clients to feel comfortable with us and that's why the relationship with them is very important to us. We want every customer to become a lifelong friend of the company. Most of our clients are premium coaches, meaning they are in the higher priced segment and expect seriousness, professionalism and quality. All of these things should reflect our business card as well. I look forward to feedback. Best regards, Tomas Wylander

```html
<!DOCTYPE html>
<html lang="en">
<head>
<meta charset="utf-8">
<title>Kestrel Media – Business Card</title>
<link href="https://fonts.googleapis.com/css2?family=Lato:wght@400;700&display=swap" rel="stylesheet">
<style>
  :root {
    --backdrop: #e6e7ea;
    --card: #ffffff;
    --navy: #1b1a6b;
    --brand-blue: #2a6fc0;
    --deep-blue: #1c2a8c;
    --ink: #2b2b2b;
    --rule: #8a8a8a;
    --shadow: rgba(20, 22, 40, 0.18);
  }
  * { box-sizing: border-box; margin: 0; padding: 0; }
  html, body {
    width: 1200px;
    height: 864px;
    overflow: hidden;
    background: var(--backdrop);
    font-family: "Lato", Arial, sans-serif;
    color: var(--ink);
  }
  .card {
    position: absolute;
    width: 600px;
    height: 343px;
    background: var(--card);
    box-shadow: 0 6px 18px var(--shadow);
  }
  .card--front { left: 300px; top: 50px; }
  .card--back  { left: 300px; top: 460px; }

  /* Brand block: plain square + name */
  .brand {
    position: absolute;
    display: flex;
    flex-direction: column;
    align-items: flex-start;
  }
  .brand__mark {
    background: linear-gradient(135deg, var(--deep-blue), var(--brand-blue));
  }
  .brand__name {
    font-weight: 700;
    color: var(--navy);
    line-height: 1;
    white-space: nowrap;
  }
  .brand__tagline {
    font-weight: 400;
    color: var(--brand-blue);
    letter-spacing: 0.04em;
    line-height: 1.2;
    white-space: nowrap;
  }

  .card--front .brand { left: 120px; top: 64px; }
  .card--front .brand__mark { width: 170px; height: 120px; }
  .card--front .brand__name { font-size: 50px; margin-top: 8px; }
  .card--front .brand__tagline { font-size: 22px; margin-top: 6px; }

  .card--back .brand { left: 330px; top: 26px; }
  .card--back .brand__mark { width: 140px; height: 82px; }
  .card--back .brand__name { font-size: 32px; margin-top: 6px; }
  .card--back .brand__tagline { font-size: 15px; margin-top: 4px; }

  .person { position: absolute; left: 66px; top: 100px; }
  .person__name {
    font-size: 20px;
    font-weight: 700;
    color: var(--navy);
    letter-spacing: 0.03em;
    text-transform: uppercase;
  }
  .person__role {
    font-size: 14px;
    letter-spacing: 0.04em;
    text-transform: uppercase;
    color: var(--ink);
  }

  .divider {
    position: absolute;
    left: 60px;
    right: 60px;
    top: 190px;
    height: 1px;
    background: var(--rule);
  }

  .address {
    position: absolute;
    left: 50px;
    top: 214px;
    display: flex;
    gap: 8px;
    font-size: 15px;
    line-height: 1.3;
  }
  .contacts {
    position: absolute;
    right: 44px;
    top: 222px;
    list-style: none;
    font-size: 15px;
    line-height: 1.3;
  }
  .contacts li {
    display: flex;
    justify-content: flex-end;
    align-items: center;
    gap: 6px;
  }
  .icon {
    width: 15px;
    height: 15px;
    flex: none;
  }
  .icon circle.ring { fill: none; stroke: var(--navy); stroke-width: 1.6; }
  .icon .glyph { fill: none; stroke: var(--navy); stroke-width: 1.4; stroke-linecap: round; stroke-linejoin: round; }
</style>
</head>
<body>

<section class="card card--front" aria-label="Card front">
  <div class="brand">
    <div class="brand__mark"></div>
    <div class="brand__name">Kestrel Media</div>
    <div class="brand__tagline">Online Marketing Services</div>
  </div>
</section>

<section class="card card--back" aria-label="Card back">
  <div class="person">
    <p class="person__name">Tomas Wylander</p>
    <p class="person__role">Managing Director</p>
  </div>

  <div class="brand">
    <div class="brand__mark"></div>
    <div class="brand__name">Kestrel Media</div>
    <div class="brand__tagline">Online Marketing Services</div>
  </div>

  <div class="divider"></div>

  <div class="address">
    <svg class="icon" viewBox="0 0 16 16" aria-hidden="true">
      <circle class="ring" cx="8" cy="8" r="7"/>
      <path class="glyph" d="M8 12 C6 9.5 5.5 8.5 5.5 7 A2.5 2.5 0 0 1 10.5 7 C10.5 8.5 10 9.5 8 12 Z"/>
    </svg>
    <p>17, Harbour Lane,<br>Westfield, 45810<br>Country Name</p>
  </div>

  <ul class="contacts">
    <li>444 555 7120
      <svg class="icon" viewBox="0 0 16 16" aria-hidden="true">
        <circle class="ring" cx="8" cy="8" r="7"/>
        <path class="glyph" d="M5.5 4.5 L7 6 L6 7.2 C6.6 8.4 7.6 9.4 8.8 10 L10 9 L11.5 10.5 L10.6 11.5 C8 11.2 4.8 8 4.5 5.4 Z"/>
      </svg>
    </li>
    <li>888 555 2091
      <svg class="icon" viewBox="0 0 16 16" aria-hidden="true">
        <circle class="ring" cx="8" cy="8" r="7"/>
        <rect class="glyph" x="5.5" y="4" width="5" height="8" rx="1"/>
      </svg>
    </li>
    <li>hello@kestrelmedia.com
      <svg class="icon" viewBox="0 0 16 16" aria-hidden="true">
        <circle class="ring" cx="8" cy="8" r="7"/>
        <rect class="glyph" x="4.5" y="5.5" width="7" height="5"/>
        <path class="glyph" d="M4.5 5.5 L8 8.3 L11.5 5.5"/>
      </svg>
    </li>
    <li>www.kestrelmedia.com
      <svg class="icon" viewBox="0 0 16 16" aria-hidden="true">
        <circle class="ring" cx="8" cy="8" r="7"/>
        <circle class="glyph" cx="8" cy="8" r="3.8"/>
        <path class="glyph" d="M4.2 8 H11.8 M8 4.2 C6.5 6 6.5 10 8 11.8 M8 4.2 C9.5 6 9.5 10 8 11.8"/>
      </svg>
    </li>
  </ul>
</section>

</body>
</html>
```